Driving-coach/trainer who wants to inform about the offer and how I can help people to drive more re

I need a flyer that informs potential customers about my offer.

DL size 210 mm x 99 mm, vertical!

I'm a trainer/coach who helps people to drive a car more relaxed, without fear and more confident.

It's a one to one training. I do train people in their own car. It gets people their freedom back to go where and when they like to go by own car...

Target Market(s)

People (man an woman) who are afraid of driving a car, or are very stressed while driving....

Industry/Entity Type

Life Coaching

Font styles to use
Sans Serif

Colors
acd136

Requirements
Must have
• Page 1:
• -my offer (see text-pdf)
• -three fotos (see attached files "Pixmarra") of people who are satisfied with my offer
• Page 2:
• -advantages in the work with me.
• -contact information
• -and a picture of me (see attached file) next to the contact information or the advantages of my work
• -my logo (see attached file) on Page 1 + 2
• -i like a "clear" and structured layout. "Less is more"

```html
<!DOCTYPE html>
<html lang="de">
<head>
<meta charset="utf-8">
<title>Fahrangst erfolgreich loswerden – Flyer</title>
<link href="https://fonts.googleapis.com/css2?family=Source+Sans+3:wght@400;600;700&display=swap" rel="stylesheet">
<style>
  :root {
    --backdrop: #1c1c1c;
    --green: #5aad34;
    --green-deep: #1d9e55;
    --green-text: #2f8f2a;
    --green-name: #6ab84a;
    --panel: #ececec;
    --white: #ffffff;
    --ink: #2b2b2b;
    --swoosh: #8a8a8a;
  }
  * { box-sizing: border-box; margin: 0; padding: 0; }
  html, body { width: 1200px; height: 2400px; overflow: hidden; background: var(--backdrop); }
  body { position: relative; font-family: "Source Sans 3", Arial, sans-serif; }

  .flyer {
    position: absolute; left: 106px; top: 150px;
    width: 988px; height: 2100px;
    background: var(--white); overflow: hidden;
  }
  .flyer-art { position: absolute; left: 0; top: 0; }

  .headline {
    position: absolute; left: 54px; top: 640px;
    color: var(--white); font-weight: 700;
    font-size: 68px; line-height: 68px; letter-spacing: 1px;
    text-transform: uppercase;
  }
  .questions {
    position: absolute; left: 54px; top: 905px; width: 620px;
    color: var(--white); font-weight: 700; font-size: 39px; line-height: 48px;
  }
  .questions p + p { margin-top: 22px; }

  .badge {
    position: absolute; border-radius: 50%;
    background: var(--green-deep); color: var(--white);
    font-weight: 700; text-align: center;
    display: flex; align-items: center; justify-content: center;
  }
  .badge-main {
    left: 616px; top: 936px; width: 328px; height: 328px;
    border: 8px solid var(--white);
    font-size: 50px; line-height: 54px;
    box-shadow: 0 4px 10px rgba(0,0,0,.25);
  }
  .badge-small {
    left: 702px; top: 1800px; width: 180px; height: 180px;
    background: var(--green); font-size: 27px; line-height: 30px;
  }

  .situations-title {
    position: absolute; left: 60px; top: 1290px;
    color: var(--green-text); font-size: 36px; font-weight: 400;
  }
  .situation-list {
    position: absolute; top: 1358px; list-style: none;
    font-size: 28.5px; line-height: 34px; color: var(--ink);
  }
  .situation-list.left { left: 54px; width: 420px; }
  .situation-list.right { left: 494px; width: 440px; }
  .situation-list li { position: relative; padding-left: 40px; margin-bottom: 24px; }
  .situation-list .tick { position: absolute; left: 0; top: 3px; width: 32px; height: 32px; }
  .situation-list strong { font-weight: 700; }
  .situation-list .hl { color: var(--green-text); font-weight: 700; }

  .coach-name {
    position: absolute; left: 66px; top: 1930px;
    color: var(--green-name); font-size: 58px; font-weight: 400; letter-spacing: 4px;
  }
  .coach-title {
    position: absolute; left: 66px; top: 2008px;
    color: var(--green-name); font-size: 37px; font-weight: 400; letter-spacing: 4px;
  }
</style>
</head>
<body>
<main class="flyer">
  <svg class="flyer-art" width="988" height="2100" viewBox="0 0 988 2100">
    <defs>
      <linearGradient id="photoMain" x1="0" y1="0" x2="1" y2="1">
        <stop offset="0" stop-color="#c9c39a"/>
        <stop offset="0.45" stop-color="#e8c7a8"/>
        <stop offset="1" stop-color="#b9bcc2"/>
      </linearGradient>
      <linearGradient id="photoCircle" x1="0" y1="0" x2="1" y2="1">
        <stop offset="0" stop-color="#c89a6a"/>
        <stop offset="0.55" stop-color="#e2c3a6"/>
        <stop offset="1" stop-color="#d8dde2"/>
      </linearGradient>
      <linearGradient id="swooshGrad" x1="0" y1="0" x2="1" y2="0">
        <stop offset="0" stop-color="#6f6f6f"/>
        <stop offset="0.5" stop-color="#b5b5b5"/>
        <stop offset="1" stop-color="#7c7c7c"/>
      </linearGradient>
    </defs>

    <!-- light panel -->
    <rect class="panel" x="0" y="1100" width="988" height="800" fill="var(--panel)"/>

    <!-- green body with curved lower edge -->
    <path class="green-body" d="M0 0 H988 V1170 C760 1240 380 1240 0 1130 Z" fill="var(--green)"/>
    <path class="green-swoosh" d="M0 1140 C380 1252 760 1252 988 1182" fill="none" stroke="url(#swooshGrad)" stroke-width="22"/>

    <!-- main photo -->
    <path d="M150 0 H988 V760 C820 720 560 680 340 560 C230 500 170 420 150 340 Z"
          fill="url(#photoMain)" role="img" aria-label="Foto: lächelnde junge Frau lehnt aus dem Autofenster und zeigt Daumen hoch"/>
    <path class="photo-swoosh" d="M200 520 C330 640 600 720 988 780" fill="none" stroke="url(#swooshGrad)" stroke-width="26"/>
    <path d="M0 0 H150 C120 80 90 160 70 260 L0 300 Z" fill="var(--white)" opacity="0.9"/>

    <!-- circle photo -->
    <circle cx="238" cy="366" r="216" fill="var(--white)"/>
    <circle cx="238" cy="366" r="204" fill="url(#photoCircle)" role="img" aria-label="Foto: lächelnde junge Frau am Steuer eines Autos"/>

    <!-- bottom white area with green line -->
    <path class="footer" d="M0 1840 C300 1790 640 1790 988 1750 V2100 H0 Z" fill="var(--white)"/>
    <path d="M0 1840 C300 1790 640 1790 988 1750" fill="none" stroke="var(--green)" stroke-width="7"/>
  </svg>

  <h1 class="headline">Fahrangst<br>erfolgreich<br>loswerden!</h1>

  <div class="questions">
    <p>Sie wollen endlich entspannt und sicher Auto fahren?</p>
    <p>Panikattacken beim Autofahren überwinden?</p>
  </div>

  <div class="badge badge-main">Dann<br>sind Sie<br>hier<br>richtig!</div>

  <h2 class="situations-title">Kommt Ihnen eine dieser Situationen bekannt vor?</h2>

  <ul class="situation-list left">
    <li>
      <svg class="tick" viewBox="0 0 32 32"><circle cx="16" cy="16" r="13" fill="none" stroke="var(--green-text)" stroke-width="3"/><path d="M9 16 l5 5 l9 -10" fill="none" stroke="var(--green-text)" stroke-width="3.5" stroke-linecap="round" stroke-linejoin="round"/></svg>
      <strong>Angst oder Panikattacken</strong> begleiten Sie beim Autofahren. Vielleicht <strong>vermeiden</strong> Sie deshalb das Autofahren komplett. - Sie möchten <span class="hl">angstfrei und/ oder ohne Panikattacken</span> fahren.
    </li>
    <li>
      <svg class="tick" viewBox="0 0 32 32"><circle cx="16" cy="16" r="13" fill="none" stroke="var(--green-text)" stroke-width="3"/><path d="M9 16 l5 5 l9 -10" fill="none" stroke="var(--green-text)" stroke-width="3.5" stroke-linecap="round" stroke-linejoin="round"/></svg>
      Sie <strong>trauen sich das Autofahren nicht (mehr) zu.</strong> - Sie wünschen sich, <span class="hl">sicher, entspannt und stressfrei Auto zu fahren.</span>
    </li>
  </ul>

  <ul class="situation-list right">
    <li>
      <svg class="tick" viewBox="0 0 32 32"><circle cx="16" cy="16" r="13" fill="none" stroke="var(--green-text)" stroke-width="3"/><path d="M9 16 l5 5 l9 -10" fill="none" stroke="var(--green-text)" stroke-width="3.5" stroke-linecap="round" stroke-linejoin="round"/></svg>
      <strong>Autofahren</strong> erleben Sie unter h<strong>oher Anspannung und Stress.</strong> - Sie wünschen sich, Autofahren <span class="hl">sicher und entspannt</span> zu erleben.
    </li>
    <li>
      <svg class="tick" viewBox="0 0 32 32"><circle cx="16" cy="16" r="13" fill="none" stroke="var(--green-text)" stroke-width="3"/><path d="M9 16 l5 5 l9 -10" fill="none" stroke="var(--green-text)" stroke-width="3.5" stroke-linecap="round" stroke-linejoin="round"/></svg>
      Bestimmte Situationen (z.B. <strong>Autobahn, Baustellen, Stadtvekehr</strong>...) bereiten Ihnen <strong>großen Stress.</strong> - Sie möchten diese Situationen <span class="hl">souveräner</span> meistern.
    </li>
  </ul>

  <div class="badge badge-small">Das muss<br>nicht so<br>bleiben!</div>

  <p class="coach-name">Carina Lindqvist</p>
  <p class="coach-title">Fahrangst-Bewältigungs-Coach</p>
</main>
</body>
</html>
```